Business Cards Design for the electrical wholesaler: clean bold dynamic :)

We need a business card design that would follow our latest brand guidelines. As an electrical wholesaler we want to bring a fresh look and feel into the industry. The design should be clean bold and dynamic. It should come alive with the renewed energy of our green colour. Our grey colour should keep things balanced and complement the notion of maturity and responsibility. We employ Lato as a corporate font however are not bound by this font and we’re open to interpretation here.

Target Market(s)

Electrical contractors

Industry/Entity Type

Business

Contact Information for Business Card

Logo
Name & Surname: Olena Dovbush
Job Title: Director of Marketing
Email: helen.dovbush@mailvane.example
Cell phone: XXX.XXX.XXXX
Address: 20917 - 87 Ave. Edmonton, AB, Canada. T6K 2R8
Business Phone: 780.555.0187
Website: www.qorvil.example

Font styles to use
Other font styles liked:
• Lato

Requirements
Must have
• Logo & website
Nice to have
• Brand elements - some of them you may find in the attached Brand Guidelines (e.g. three lines on the background signifying "W")

```html
<!DOCTYPE html>
<html lang="en">
<head>
<meta charset="utf-8">
<title>QV Business Card – Design 1 Comp</title>
<link href="https://fonts.googleapis.com/css2?family=Lato:wght@400;700;900&display=swap" rel="stylesheet">
<style>
  :root {
    --page-bg: #ffffff;
    --ink: #111111;
    --card-grey: #cccccc;
    --brand-grey: #58585a;
    --brand-green: #8cc63f;
    --brand-orange: #f07008;
  }
  * { box-sizing: border-box; margin: 0; padding: 0; }
  html, body {
    width: 1200px;
    height: 547px;
    overflow: hidden;
    background: var(--page-bg);
    font-family: "Lato", sans-serif;
    color: var(--ink);
  }
  .sheet { position: relative; width: 1200px; height: 547px; }

  .sheet-title {
    position: absolute;
    left: 51px;
    top: 49px;
    font-size: 14px;
    font-weight: 400;
    letter-spacing: 0.2px;
  }

  .card {
    position: absolute;
    top: 201px;
    width: 388px;
    height: 221px;
  }
  .card--front { left: 150px; background: var(--card-grey); }
  .card--back  { left: 622px; background: var(--brand-orange); }

  .side-label {
    position: absolute;
    top: 451px;
    font-size: 14px;
    transform: translateX(-50%);
  }
  .side-label--front { left: 318px; }
  .side-label--back  { left: 809px; font-size: 12px; top: 455px; }

  /* wordmark */
  .wordmark {
    position: absolute;
    display: flex;
    align-items: center;
    font-family: "Lato", sans-serif;
    font-weight: 700;
    color: var(--brand-grey);
    letter-spacing: -0.5px;
  }
  .wordmark__square { background: var(--brand-green); flex: none; }
  .wordmark--front {
    left: 50%;
    top: 14px;
    transform: translateX(-50%);
    font-size: 42px;
    gap: 10px;
  }
  .wordmark--front .wordmark__square { width: 34px; height: 34px; }
  .wordmark--back {
    left: 50%;
    top: 50%;
    transform: translate(-50%, -52%);
    font-size: 58px;
    gap: 14px;
  }
  .wordmark--back .wordmark__square { width: 46px; height: 46px; }

  /* holder */
  .holder {
    position: absolute;
    top: 80px;
    left: 0;
    width: 100%;
    text-align: center;
  }
  .holder__name { font-size: 17px; font-weight: 900; line-height: 20px; }
  .holder__role { font-size: 12.5px; line-height: 15px; }

  .address {
    position: absolute;
    left: 16px;
    top: 131px;
    font-size: 12.5px;
    line-height: 13.5px;
    font-style: normal;
  }
  .website {
    position: absolute;
    left: 16px;
    top: 185px;
    font-size: 12.5px;
  }
  .phones {
    position: absolute;
    right: 12px;
    top: 137px;
    text-align: right;
    font-size: 14px;
    line-height: 16px;
  }
  .email {
    position: absolute;
    right: 12px;
    top: 182px;
    font-size: 13px;
  }
</style>
</head>
<body>
<main class="sheet">
  <h1 class="sheet-title">QV BUSINESS CARD - DESIGN 1 COMP</h1>

  <section class="card card--front" aria-label="Card front">
    <div class="wordmark wordmark--front"><span class="wordmark__square"></span>qorvil</div>
    <div class="holder">
      <p class="holder__name">OLENA DOVBUSH</p>
      <p class="holder__role">DIRECTOR OF MARKETING</p>
    </div>
    <address class="address">20917 - 87 Avenue<br>Edmonton, AB, Canada<br>T6K 2R8</address>
    <p class="website">www.qorvil.example</p>
    <p class="phones">Cell: XXX.XXX.XXXX<br>Office: 780.555.0187</p>
    <p class="email">helen.dovbush@mailvane.example</p>
  </section>
  <p class="side-label side-label--front">FRONT</p>

  <section class="card card--back" aria-label="Card back">
    <div class="wordmark wordmark--back"><span class="wordmark__square"></span>qorvil</div>
  </section>
  <p class="side-label side-label--back">BACK</p>
</main>
</body>
</html>
```